pressure washing advertisment

I would like front and back designed post cards. we offer pressure washing services for residential customers. I want to highlight before and after pictures as examples of our more popular services. I would also like to have our email www.brightlanewashco.com and the facebook and Instagram logo somewhere. you can also include all major credit card logos as acceptable payments. I have attached our logo along with before and after pictures. also feel free to go to my website for any additional information that should be added to the post card. lastly I want a small promotion of $25 off any service somewhere.<br/><br/>Thank you!!

Target Market(s)

homeowners

Industry/Entity Type

Cleaning Service

Font styles to use
Serif
Sans Serif

Colors

Designer to choose colors to be used in the design.

Requirements
Must have
• before and after pictures with website and logo
Nice to have
• clean look that flows

```html
<!DOCTYPE html>
<html lang="en">
<head>
<meta charset="utf-8">
<title>Bright Lane Wash Co. Postcard</title>
<link href="https://fonts.googleapis.com/css2?family=Open+Sans:wght@400;600;700;800&display=swap" rel="stylesheet">
<style>
:root{
  --red:#e01e26;
  --blue:#0f4183;
  --navy:#123a73;
  --ink:#3b3b3b;
  --white:#ffffff;
  --silver-a:#f4f4f4;
  --silver-b:#c9c9c9;
  --backdrop:#e6e6e6;
}
*{box-sizing:border-box;margin:0;padding:0}
html,body{width:689px;height:1200px;overflow:hidden}
body{background:var(--backdrop);font-family:"Open Sans",Arial,sans-serif;position:relative;color:var(--ink)}
.card{position:absolute;left:24px;width:640px;height:427px;background:var(--white);overflow:hidden;box-shadow:0 6px 18px rgba(0,0,0,.25)}
.card--front{top:118px}
.card--back{top:652px}
.abs{position:absolute}
.photo{position:absolute}
.photo--house{left:0;top:0;width:372px;height:241px;clip-path:polygon(0 0,100% 0,91% 100%,0 100%);background:linear-gradient(180deg,#9fb3cf 0%,#c9c2b4 45%,#8a8271 70%,#4f7a32 100%)}
.photo--before{left:0;top:247px;width:160px;height:115px;clip-path:polygon(0 0,100% 0,93% 100%,0 100%);background:linear-gradient(135deg,#c8c2b0,#7e7a6a 60%,#3c4a55)}
.photo--after{left:158px;top:247px;width:134px;height:115px;clip-path:polygon(9% 0,100% 0,92% 100%,0 100%);background:linear-gradient(135deg,#e0ddd2,#b6b2a4 60%,#3c4a55)}
.tag{position:absolute;background:var(--red);color:var(--white);font-weight:700;font-size:11px;padding:2px 10px 2px 14px;clip-path:polygon(8% 0,100% 0,100% 100%,0 100%)}
.brand{font-weight:800;color:var(--blue);letter-spacing:.3px}
.brand-mark{display:inline-block;width:14px;height:14px;border-radius:50%;background:var(--red);vertical-align:middle;margin-right:6px}
.front-brand{right:24px;top:20px;font-size:17px}
.headline{right:24px;top:68px;text-align:right;line-height:1.05}
.headline__big{font-size:27px;font-weight:800;color:#3a3a3a;letter-spacing:.5px}
.headline__red{font-size:13.5px;font-weight:800;color:var(--red)}
.headline__blue{font-size:11px;font-weight:800;color:var(--blue);margin-top:2px}
.headline__place{font-size:7.5px;color:#555;margin-top:2px}
.tab{right:30px;top:142px;width:140px;height:28px;background:linear-gradient(90deg,#bdbdbd,#efefef);clip-path:polygon(8% 0,100% 0,92% 100%,0 100%);font-weight:800;font-size:13px;color:#2e2e2e;display:flex;align-items:center;justify-content:center}
.band-blue{left:335px;top:170px;width:305px;height:119px;background:var(--blue);clip-path:polygon(7% 0,100% 0,100% 100%,0 100%)}
.band-red{left:285px;top:289px;width:355px;height:101px;background:var(--red);clip-path:polygon(5% 0,100% 0,100% 100%,0 100%)}
.service-title{font-weight:800;color:var(--white);font-size:13.5px;letter-spacing:.2px}
.service-list{list-style:none;color:var(--white);font-size:10.5px;line-height:16px;text-align:right}
.service-list li::after{content:"";display:inline-block;width:4px;height:4px;border-radius:50%;background:var(--white);margin-left:7px;vertical-align:middle}
.res-title{right:28px;top:180px}
.res-list{right:28px;top:200px}
.com-title{right:28px;top:297px}
.com-list-a{right:140px;top:322px}
.com-list-b{right:28px;top:322px}
.badge{left:270px;top:202px;width:84px;height:84px;border-radius:50%;background:radial-gradient(circle at 40% 35%,#fff 55%,#d6d6d6);border:4px solid #e8e8e8;box-shadow:0 2px 5px rgba(0,0,0,.3);text-align:center;padding-top:18px}
.badge__amount{font-size:22px;font-weight:800;color:var(--red);line-height:1}
.badge__amount small{font-size:9px}
.badge__note{font-size:8.5px;font-weight:600;color:#333}
.strip{left:0;top:368px;width:640px;height:59px;background:linear-gradient(90deg,#d6d6d6,#f6f6f6 40%,#cfcfcf)}
.phone-icon{position:absolute;width:30px;height:30px}
.front-phone{left:74px;top:378px;font-size:29px;font-weight:800;color:var(--red);letter-spacing:.5px}
.contact{font-size:8px;color:#333;line-height:14px}
.contact b{color:var(--red);font-weight:600}
.dot{display:inline-block;width:8px;height:8px;border-radius:50%;border:1.5px solid var(--red);margin-right:5px;vertical-align:middle}
.front-contact{left:302px;top:384px}
.divider{left:452px;top:384px;width:1px;height:28px;background:var(--red)}
.address{left:462px;top:384px;font-size:8px;font-weight:700;color:#222;line-height:13px}
.pin{position:absolute;left:-0px}
.social{width:13px;height:13px;border-radius:50%;background:var(--blue)}
/* back */
.back-head{left:0;top:0;width:363px;height:55px;background:var(--red);clip-path:polygon(0 0,100% 0,97% 100%,0 100%);color:var(--white);font-size:18px;padding:12px 0 0 41px}
.back-head b{font-weight:800}
.back-perks{left:0;top:55px;width:352px;height:106px;background:linear-gradient(90deg,#f0f0f0,#c6c6c6);clip-path:polygon(0 0,100% 0,94% 100%,0 100%);padding:12px 0 0 42px}
.back-perks ul{list-style:none;font-size:11px;font-weight:600;color:#333;line-height:23px}
.back-perks li::before{content:"";display:inline-block;width:5px;height:5px;border-radius:50%;background:var(--blue);margin-right:12px;vertical-align:middle}
.back-gallery{left:0;top:161px;width:331px;height:215px;background:var(--blue);clip-path:polygon(0 0,100% 0,84% 100%,0 100%)}
.thumb{position:absolute;border:3px solid var(--white)}
.thumb--drive-before{left:38px;top:186px;width:118px;height:78px;background:linear-gradient(135deg,#5b6a4e,#b9b6ad 55%,#8a877e);clip-path:polygon(3% 0,100% 0,97% 100%,0 100%)}
.thumb--drive-after{left:162px;top:186px;width:122px;height:78px;background:linear-gradient(135deg,#4e5d43,#9c9990 55%,#6e6b63);clip-path:polygon(3% 0,100% 0,97% 100%,0 100%)}
.thumb--lawn-before{left:22px;top:282px;width:120px;height:78px;background:linear-gradient(135deg,#a67c3c,#6f8a3a 55%,#3e5a22);clip-path:polygon(3% 0,100% 0,97% 100%,0 100%)}
.thumb--lawn-after{left:148px;top:282px;width:120px;height:78px;background:linear-gradient(135deg,#d5d3cc,#6f8a3a 50%,#3e5a22);clip-path:polygon(3% 0,100% 0,97% 100%,0 100%)}
.back-footer{left:0;top:376px;width:266px;height:51px;background:linear-gradient(90deg,#d9d9d9,#f2f2f2);clip-path:polygon(0 0,100% 0,96% 100%,0 100%)}
.back-phone{left:37px;top:394px;font-size:12.5px;font-weight:800;color:var(--red)}
.back-contact{left:130px;top:385px;font-size:7px;line-height:13px}
.back-brand{left:382px;top:40px;font-size:16px}
.stamp{left:549px;top:28px;width:74px;height:68px;border:1.5px solid #444}
.address-line{left:382px;width:242px;height:1px;background:#555}
</style>
</head>
<body>

<section class="card card--front" aria-label="Postcard front">
  <div class="photo photo--house" role="img" aria-label="Photo of a clean two-storey house with lit windows at dusk"></div>
  <div class="photo photo--before" role="img" aria-label="Before photo: pressure wand aimed at dirty siding"></div>
  <div class="photo photo--after" role="img" aria-label="After photo: pressure wand aimed at clean siding"></div>
  <span class="tag" style="left:78px;top:343px">BEFORE</span>
  <span class="tag" style="left:220px;top:343px">AFTER</span>

  <div class="abs brand front-brand"><span class="brand-mark"></span>BRIGHT LANE WASH CO.</div>
  <div class="abs headline">
    <div class="headline__big">PROFESSIONAL</div>
    <div class="headline__red">RESIDENTIAL &amp; COMMERCIAL</div>
    <div class="headline__blue">PRESSURE WASHING CONTRACTOR</div>
    <div class="headline__place">IN COASTAL BAY, FL</div>
  </div>

  <div class="abs band-blue"></div>
  <div class="abs tab">WHAT WE DO</div>
  <div class="abs service-title res-title">RESIDENTIAL PRESSURE WASHING</div>
  <ul class="abs service-list res-list">
    <li>Soft Wash House Washing</li>
    <li>Driveway &amp; Concrete Cleaning</li>
    <li>Gutter Cleaning &amp; Brightening</li>
    <li>Deck &amp; Fence Cleaning</li>
  </ul>

  <div class="abs band-red"></div>
  <div class="abs service-title com-title">COMMERCIAL PRESSURE WASHING</div>
  <ul class="abs service-list com-list-a">
    <li>Soft Wash House Washing</li>
    <li>Parking Lot Cleaning</li>
    <li>Surface Cleaning</li>
  </ul>
  <ul class="abs service-list com-list-b">
    <li>Gum</li>
    <li>Graffiti</li>
    <li>Rust Removal</li>
  </ul>

  <div class="abs badge">
    <div class="badge__amount">$25<small>OFF</small></div>
    <div class="badge__note">ANY SERVICE</div>
  </div>

  <div class="abs strip"></div>
  <svg class="phone-icon" style="left:22px;top:383px" viewBox="0 0 30 30" aria-hidden="true">
    <circle cx="15" cy="15" r="13" fill="none" stroke="var(--blue)" stroke-width="2"/>
    <path d="M10 9c1-1 2-1 2.5 0l1.5 2.5c.4.7 0 1.3-.6 1.8l-.8.6c.8 1.8 2.2 3.2 4 4l.6-.8c.5-.6 1.1-1 1.8-.6l2.5 1.5c1 .5 1 1.5 0 2.5-1.5 1.5-4 1.5-7-1.5s-5-6-4.5-10z" fill="var(--red)"/>
  </svg>
  <div class="abs front-phone">904-555-0173</div>

  <div class="abs contact front-contact">
    <div><span class="dot"></span><b>hello</b>@brightlanewashco.com</div>
    <div><span class="dot"></span>www.<b>brightlanewashco</b>.com</div>
  </div>
  <div class="abs divider"></div>
  <svg class="abs" style="left:440px;top:386px" width="9" height="12" viewBox="0 0 9 12" aria-hidden="true"><path d="M4.5 0A4.5 4.5 0 0 0 0 4.5C0 8 4.5 12 4.5 12S9 8 9 4.5A4.5 4.5 0 0 0 4.5 0z" fill="var(--red)"/><circle cx="4.5" cy="4.5" r="1.6" fill="#fff"/></svg>
  <div class="abs address" style="left:459px">47 Harbor Pine Way<br>Coastal Bay, FL 32099</div>
  <div class="abs divider" style="left:580px"></div>
  <div class="abs social" style="left:588px;top:392px"></div>
  <div class="abs social" style="left:605px;top:392px"></div>
</section>

<section class="card card--back" aria-label="Postcard back">
  <div class="abs back-head"><b>EXTERIOR CLEANING</b> EXPERTS</div>
  <div class="abs back-perks">
    <ul>
      <li>Experienced &amp; Friendly Professionals</li>
      <li>Free Estimates</li>
      <li>100% Satisfaction Guaranteed</li>
      <li>Residential &amp; Commercial</li>
    </ul>
  </div>
  <div class="abs back-gallery"></div>
  <div class="thumb thumb--drive-before" role="img" aria-label="Before photo: stained concrete driveway"></div>
  <div class="thumb thumb--drive-after" role="img" aria-label="After photo: cleaned concrete driveway"></div>
  <div class="thumb thumb--lawn-before" role="img" aria-label="Before photo: grimy curb edge by lawn"></div>
  <div class="thumb thumb--lawn-after" role="img" aria-label="After photo: clean curb edge by lawn"></div>
  <span class="tag" style="left:98px;top:248px;font-size:10px">BEFORE</span>
  <span class="tag" style="left:230px;top:248px;font-size:10px">AFTER</span>
  <span class="tag" style="left:84px;top:344px;font-size:10px">BEFORE</span>
  <span class="tag" style="left:212px;top:343px;font-size:10px">AFTER</span>

  <div class="abs back-footer"></div>
  <svg class="abs" style="left:20px;top:393px" width="13" height="13" viewBox="0 0 30 30" aria-hidden="true">
    <circle cx="15" cy="15" r="13" fill="none" stroke="var(--blue)" stroke-width="2.5"/>
    <path d="M10 9c1-1 2-1 2.5 0l1.5 2.5c.4.7 0 1.3-.6 1.8l-.8.6c.8 1.8 2.2 3.2 4 4l.6-.8c.5-.6 1.1-1 1.8-.6l2.5 1.5c1 .5 1 1.5 0 2.5-1.5 1.5-4 1.5-7-1.5s-5-6-4.5-10z" fill="var(--red)"/>
  </svg>
  <div class="abs back-phone">904-555-0173</div>
  <div class="abs contact back-contact">
    <div><span class="dot" style="width:7px;height:7px"></span><b>hello</b>@brightlanewashco.com</div>
    <div><span class="dot" style="width:7px;height:7px"></span>www.<b>brightlanewashco</b>.com</div>
  </div>

  <div class="abs brand back-brand"><span class="brand-mark"></span>BRIGHT LANE<br>WASH CO.</div>
  <div class="abs stamp"></div>
  <div class="abs address-line" style="top:235px"></div>
  <div class="abs address-line" style="top:273px"></div>
  <div class="abs address-line" style="top:311px"></div>
</section>

</body>
</html>
```